Lantern Hill Publicity is a new boutique Press Office with a small roster of well-chosen clients across an array of disciplines; from Art and Technology to Restaurants and Fashion. Based in Greenpoint Brooklyn, Lantern Hill Publicity achieves outstanding results through hard work, tenacity, efficiency and a sense of humor. We need a simple, versatile and classic design. We would like each side of the card to be white text on a black background.

Boutique

```html
<!DOCTYPE html>
<html lang="en">
<head>
<meta charset="utf-8">
<title>Lantern Hill Publicity — Business Card</title>
<link href="https://fonts.googleapis.com/css2?family=Libre+Baskerville&family=Open+Sans&display=swap" rel="stylesheet">
<style>
  :root {
    --backdrop: #5c5c5c;
    --card: #000000;
    --ink: #ffffff;
    --rule: #d9d9d9;
  }
  * { margin: 0; padding: 0; box-sizing: border-box; }
  html, body {
    width: 1200px;
    height: 1200px;
    overflow: hidden;
    background: var(--backdrop);
  }
  .canvas {
    position: relative;
    width: 1200px;
    height: 1200px;
  }
  .card {
    position: absolute;
    left: 258px;
    width: 685px;
    height: 387px;
    background: var(--card);
    color: var(--ink);
  }
  .card--front { top: 188px; }
  .card--back { top: 625px; }

  .wordmark {
    position: absolute;
    text-align: center;
    font-family: "Libre Baskerville", serif;
    font-weight: 400;
    color: var(--ink);
    line-height: 1;
  }
  .wordmark__name {
    display: block;
    font-size: 27px;
    letter-spacing: 0.16em;
    margin-right: -0.16em;
  }
  .wordmark__line {
    display: block;
    font-size: 11px;
    letter-spacing: 0.62em;
    margin-right: -0.62em;
    margin-top: 12px;
  }
  .card--front .wordmark {
    left: 0;
    right: 0;
    top: 170px;
  }
  .card--back .wordmark {
    left: 30px;
    width: 300px;
    top: 172px;
  }

  .divider {
    position: absolute;
    left: 349px;
    top: 83px;
    width: 1px;
    height: 220px;
    background: linear-gradient(to bottom, transparent, var(--rule) 15%, var(--rule) 85%, transparent);
  }

  .contact {
    position: absolute;
    left: 382px;
    top: 134px;
  }
  .contact__name {
    font-family: "Libre Baskerville", serif;
    font-weight: 400;
    font-size: 25px;
    line-height: 1;
    margin-bottom: 26px;
  }
  .contact__list {
    list-style: none;
    font-family: "Open Sans", sans-serif;
    font-size: 16px;
    line-height: 23px;
  }
  .contact__item {
    display: flex;
    align-items: center;
    gap: 6px;
  }
  .contact__icon {
    width: 13px;
    height: 13px;
    fill: var(--ink);
    flex: none;
  }
</style>
</head>
<body>
<main class="canvas">
  <section class="card card--front" aria-label="Card front">
    <div class="wordmark">
      <span class="wordmark__name">LANTERN HILL</span>
      <span class="wordmark__line">PUBLICITY</span>
    </div>
  </section>

  <section class="card card--back" aria-label="Card back">
    <div class="wordmark">
      <span class="wordmark__name">LANTERN HILL</span>
      <span class="wordmark__line">PUBLICITY</span>
    </div>
    <div class="divider"></div>
    <div class="contact">
      <p class="contact__name">Mara Reyes</p>
      <ul class="contact__list">
        <li class="contact__item">
          <svg class="contact__icon" viewBox="0 0 16 16" aria-hidden="true"><path d="M1 6c0-2 3-3.5 7-3.5S15 4 15 6v1.3h-3.2V5.8C10.5 5.4 5.5 5.4 4.2 5.8v1.5H1z"/><path d="M3.5 8.3 5.5 6.5h5l2 1.8V14h-9z M8 8.5a2 2 0 1 0 0 4 2 2 0 0 0 0-4z"/></svg>
          <span>(00) 000-0000</span>
        </li>
        <li class="contact__item">
          <svg class="contact__icon" viewBox="0 0 16 16" aria-hidden="true"><path d="M1 4h14v.6L8 9.2 1 4.6z"/><path d="M1 6l7 4.6L15 6v6H1z"/></svg>
          <span>mreyes@lanternhill.com</span>
        </li>
        <li class="contact__item">
          <svg class="contact__icon" viewBox="0 0 16 16" aria-hidden="true"><circle cx="8" cy="8" r="6.3" fill="none" stroke="#fff" stroke-width="1.3"/><ellipse cx="8" cy="8" rx="2.6" ry="6.3" fill="none" stroke="#fff" stroke-width="1.1"/><path d="M1.7 8h12.6M2.8 5h10.4M2.8 11h10.4" stroke="#fff" stroke-width="1"/></svg>
          <span>www.lanternhill.com</span>
        </li>
      </ul>
    </div>
  </section>
</main>
</body>
</html>
```